Local Motorsports Photography Business Card Design

Looking for a Logo and Business Card design for my father who is a local photographer based in Perth operating under the business name "KLV Photography". Specializing in Motorsports (Torque Racers/Gridcycles/Vorlen Rally) and events photography.
Would like it to look professional, while still maintaining a local/personal feel. Color\Design of the Logo and Card are open to your own interpretation, but should limit the color scheme to around 2-3 colors.
Design should be a logo one side and contact details on the rear. The website currently is very simple and a generic template and should not be used as a basis for design.
Industry/Entity Type
Business
Contact Information for Business Card
Name: Gareth Pindle
Website: www.klvphotography-example.com.au
Email: gareth@klvphotography-example.com.au
Phone: 0455 917 263
Look and feel
Each slider illustrates characteristics of the customer's brand and the style your logo design should communicate.

```html
<!DOCTYPE html>
<html lang="en">
<head>
<meta charset="utf-8">
<title>KLV Photography – Business Card</title>
<link href="https://fonts.googleapis.com/css2?family=Open+Sans:ital,wght@0,400;0,600;1,600&display=swap" rel="stylesheet">
<style>
  :root {
    --bg: #e4e5e6;
    --card: #ffffff;
    --green: #109a4e;
    --green-light: #8cc63f;
    --text: #4a4a4a;
    --muted: #6d6d6d;
  }
  * { box-sizing: border-box; margin: 0; padding: 0; }
  html, body {
    width: 1200px; height: 772px; overflow: hidden;
    background: var(--bg);
    font-family: "Open Sans", Arial, sans-serif;
  }
  .sheet {
    width: 1200px; height: 772px;
    display: flex; align-items: center; justify-content: center; gap: 60px;
  }
  .card {
    width: 525px; height: 300px;
    background: var(--card);
    position: relative;
    box-shadow: 0 6px 18px rgba(0,0,0,.18);
    overflow: hidden;
  }
  .brand {
    display: flex; align-items: center; gap: 12px;
    color: var(--green);
    font-weight: 600;
    letter-spacing: .5px;
  }
  .brand-dot {
    border-radius: 50%;
    border: 3px solid var(--green);
    flex: none;
  }
  /* front */
  .card-front .brand {
    position: absolute; left: 50%; top: 50%;
    transform: translate(-50%, -50%);
    font-size: 30px;
  }
  .card-front .brand-dot { width: 34px; height: 34px; }
  /* back */
  .card-back .brand {
    position: absolute; right: 70px; top: 46px;
    font-size: 24px;
  }
  .card-back .brand-dot { width: 28px; height: 28px; }
  .name-band {
    position: absolute; left: 0; right: 0; top: 112px; height: 52px;
    background: var(--green);
    border-top: 4px solid var(--green-light);
    border-bottom: 4px solid var(--green-light);
    box-shadow: 0 -7px 0 -3px #fff, 0 7px 0 -3px #fff,
                0 -9px 0 -3px var(--green-light), 0 9px 0 -3px var(--green-light);
    display: flex; align-items: center; justify-content: center;
    color: #fff; font-size: 17px; font-weight: 600;
  }
  .name-band .role { font-style: italic; font-weight: 400; margin-left: 10px; }
  .contacts {
    position: absolute; left: 30px; right: 24px; top: 200px;
    display: grid; grid-template-columns: 1fr 1.35fr; row-gap: 12px; column-gap: 16px;
    font-size: 11.5px; color: var(--text);
  }
  .contact { display: flex; align-items: center; gap: 7px; white-space: nowrap; }
  .contact svg { width: 14px; height: 14px; flex: none; }
</style>
</head>
<body>
<main class="sheet">
  <section class="card card-front" aria-label="Card front">
    <div class="brand"><span class="brand-dot"></span><span>KLV Photography</span></div>
  </section>

  <section class="card card-back" aria-label="Card back">
    <div class="brand"><span class="brand-dot"></span><span>KLV Photography</span></div>
    <div class="name-band">Gareth Pindle <span class="role">| Owner / C.E.O</span></div>
    <div class="contacts">
      <div class="contact">
        <svg viewBox="0 0 14 14"><circle cx="7" cy="7" r="7" fill="#555"/><path d="M4.5 3.5l1.6 0 .6 2-1 .8a5 5 0 0 0 2 2l.8-1 2 .6v1.6c-3.5.3-6.3-2.5-6-6z" fill="#fff"/></svg>
        0455 917 263
      </div>
      <div class="contact">
        <svg viewBox="0 0 14 14"><circle cx="7" cy="7" r="7" fill="#555"/><path d="M7 3a2.5 2.5 0 0 0-2.5 2.5C4.5 7.5 7 11 7 11s2.5-3.5 2.5-5.5A2.5 2.5 0 0 0 7 3z" fill="#fff"/><circle cx="7" cy="5.5" r=".9" fill="#555"/></svg>
        Suite 4, 12 Kelm Rd, Perth WA 6000
      </div>
      <div class="contact">
        <svg viewBox="0 0 14 14"><circle cx="7" cy="7" r="7" fill="#555"/><path d="M4.5 3.5l1.6 0 .6 2-1 .8a5 5 0 0 0 2 2l.8-1 2 .6v1.6c-3.5.3-6.3-2.5-6-6z" fill="#fff"/></svg>
        0455 917 264
      </div>
      <div class="contact">
        <svg viewBox="0 0 14 14"><circle cx="7" cy="7" r="7" fill="#555"/><circle cx="7" cy="7" r="3.6" fill="none" stroke="#fff" stroke-width="1"/><path d="M3.4 7h7.2M7 3.4v7.2" stroke="#fff" stroke-width="1"/></svg>
        www.klvphotography-example.com.au
      </div>
      <div class="contact">
        <svg viewBox="0 0 14 14"><circle cx="7" cy="7" r="7" fill="#555"/><path d="M4.5 3.5l1.6 0 .6 2-1 .8a5 5 0 0 0 2 2l.8-1 2 .6v1.6c-3.5.3-6.3-2.5-6-6z" fill="#fff"/></svg>
        0455 917 265
      </div>
      <div class="contact">
        <svg viewBox="0 0 14 14"><circle cx="7" cy="7" r="7" fill="#555"/><rect x="3.5" y="4.5" width="7" height="5" fill="none" stroke="#fff" stroke-width="1"/><path d="M3.5 4.5L7 7.5l3.5-3" fill="none" stroke="#fff" stroke-width="1"/></svg>
        gareth@klvphotography-example.com.au
      </div>
    </div>
  </section>
</main>
</body>
</html>
```